Consulting Firm stationery design

Now that the ArtHive has given us a new logo we'll now need to have all our stationery designed. So we're asking for this community to help us once again.We're looking to get from you Letterheads (Header and Footer, suitable to be applied on a .docx format. Vectors are required but keep this in mind), Envelopes (Front and Back designs, back is not a must but desirable depending on your design), 9"x 12" Pocket Folders (consider design for front and back, also for pockets as well), Business Cards.An elegant design is a must have, mostly for Folders and Envelopes. The idea with this two is to stand out from others when they're handed over. Ideas are welcomed, we were thinking maybe on some texturing simulation for these.Folders will have 3 addresses and contact information. Envelopes will have 1 address and contact information.Brand Manual attached. marquesino logo has been copyrighted already. I'm also attaching the current stationary designs (these never got to be out for production but was going to be before we made the brand changes); Pocker folders page 1 to 4 (pages 2 and 4 are the pocket designs), Pages 5 and 6 (6 is the back of the envelope), Pages 7 and 8 (8 is the back of the business card). No letterhead within these designs as it just had the logo and address.

Industry/Entity Type

Business Consultant

Font styles to use
Serif
Sans Serif

Requirements
Must have
• Elegance
Nice to have
• Modern looking out of common

```html
<!DOCTYPE html>
<html lang="en">
<head>
<meta charset="utf-8">
<title>marquesino — Envelope, front and back</title>
<link rel="stylesheet" href="https://fonts.googleapis.com/css2?family=Open+Sans:wght@400;600;700&display=swap">
<style>
  :root {
    --backdrop: #e9eaeb;
    --paper: #0b0b0d;
    --paper-glow: #19191c;
    --sparkle: rgba(255,255,255,.16);
    --sparkle-soft: rgba(255,255,255,.08);
    --flap-fill: #0e0e11;
    --flap-line: #2e2e33;
    --ink-light: #f4f4f4;
    --ink-muted: #8d8d93;
    --brand-blue: #0a7bbd;
    --window: #ffffff;
    --window-ink: #1c1c1c;
  }
  * { box-sizing: border-box; margin: 0; padding: 0; }
  html, body { width: 1200px; height: 1200px; overflow: hidden; }
  body {
    background: var(--backdrop);
    font-family: "Open Sans", Arial, sans-serif;
    position: relative;
  }

  .envelope {
    position: absolute;
    left: 130px;
    width: 940px;
    height: 470px;
    background:
      radial-gradient(circle at 30% 40%, var(--sparkle) 0.6px, transparent 1.2px) 0 0 / 7px 9px,
      radial-gradient(circle at 70% 20%, var(--sparkle-soft) 0.6px, transparent 1.2px) 3px 2px / 11px 8px,
      radial-gradient(circle at 50% 80%, var(--sparkle-soft) 0.5px, transparent 1px) 1px 5px / 5px 13px,
      radial-gradient(ellipse at 55% 35%, var(--paper-glow), var(--paper) 70%);
    box-shadow: 0 10px 28px rgba(0,0,0,.28);
    overflow: hidden;
  }
  .envelope--front { top: 60px; }
  .envelope--back { top: 650px; }

  .sender {
    position: absolute;
    left: 66px;
    top: 120px;
    color: var(--ink-light);
  }
  .sender__name {
    display: flex;
    align-items: center;
    gap: 10px;
    font-weight: 700;
    font-size: 44px;
    letter-spacing: -1px;
    color: var(--brand-blue);
    margin-bottom: 34px;
  }
  .sender__dot {
    width: 14px; height: 14px;
    border-radius: 50%;
    background: var(--brand-blue);
  }
  .sender__address {
    font-size: 15px;
    line-height: 1.75;
  }
  .sender__social {
    display: flex;
    gap: 14px;
    margin-top: 14px;
    list-style: none;
  }
  .sender__social li {
    width: 24px; height: 24px;
    border-radius: 50%;
    background: var(--ink-light);
  }

  .address-window {
    position: absolute;
    right: 56px;
    top: 280px;
    width: 340px;
    height: 150px;
    background: var(--window);
    border-radius: 20px;
    padding: 38px 36px;
    color: var(--window-ink);
    font-size: 17px;
    line-height: 1.8;
  }

  .flap { position: absolute; inset: 0; width: 100%; height: 100%; }

  .web-address {
    position: absolute;
    left: 0; right: 0;
    top: 392px;
    display: flex;
    justify-content: center;
    align-items: center;
    gap: 8px;
    font-size: 22px;
    color: var(--ink-muted);
  }
  .web-address svg { width: 20px; height: 20px; }
</style>
</head>
<body>

  <section class="envelope envelope--front" aria-label="Envelope front">
    <div class="sender">
      <div class="sender__name">marquesino<span class="sender__dot"></span></div>
      <p class="sender__address">
        DO | Ave. Las Palmeras 41<br>
        Torre Ámbar, 2do Nivel<br>
        Santo Domingo, D.N.
      </p>
      <ul class="sender__social" aria-label="Social profiles">
        <li></li><li></li><li></li><li></li>
      </ul>
    </div>

    <div class="address-window">
      US | 1180 Harbor View Lane<br>
      Suite C4, Dover, DE 19901<br>
      United States
    </div>
  </section>

  <section class="envelope envelope--back" aria-label="Envelope back">
    <svg class="flap" viewBox="0 0 940 470" preserveAspectRatio="none" aria-hidden="true">
      <polygon points="80,0 160,150 790,200 940,40 940,0" fill="var(--flap-fill)" fill-opacity=".55"/>
      <polyline points="80,0 160,150 790,200 940,40" fill="none" stroke="var(--flap-line)" stroke-width="4"/>
    </svg>
    <p class="web-address">
      <svg viewBox="0 0 20 20" aria-hidden="true">
        <circle cx="10" cy="10" r="8" fill="none" stroke="#8d8d93" stroke-width="2"/>
        <path d="M2 10h16M10 2c-4 4-4 12 0 16M10 2c4 4 4 12 0 16" fill="none" stroke="#8d8d93" stroke-width="1.5"/>
      </svg>
      www.marquesino.do
    </p>
  </section>

</body>
</html>
```